Labels for fruit liqueur bottles

We are looking for a visual identity based on our logo, for fruit liqueur labels. To date, we have different liqueurs such as: lemon liqueur, orange liqueurs, mandarin liqueurs, grapefruit liqueurs. We will then create other liqueurs such as strawberry, apple or even apricot. Our goal is to have a single visual that we can adapt in different colors depending on the fruit used.

On the label there should be:
the logo
homemade
the name of the fruit (which can be changed depending on the product)
swiss-made
50cl
21°

Colors

Designer to choose colors to be used in the design.

Requirements
Must have
• a visual of liquor bottle labels, with the possibility of changing the background colors, depending on the fruit used
Nice to have
• something modern and nice to look at. We must be able to read the basic fruit in the blink of an eye. it is also possible to have a black or white or colored label background.

```html
<!DOCTYPE html>
<html lang="en">
<head>
<meta charset="utf-8">
<title>Casa Bellani – Orange Liqueur Label</title>
<link href="https://fonts.googleapis.com/css2?family=Teko:wght@400;500;600&family=Montserrat:wght@500;600&display=swap" rel="stylesheet">
<style>
  :root {
    --page-bg: #f4f4f4;
    --label-bg: #ffffff;
    --fruit: #e8922e;
    --fruit-light: #f2b15e;
    --fruit-dark: #d97e1c;
    --ink: #2f2f2f;
    --ink-soft: #5e5e5e;
    --swiss-red: #e8423c;
  }
  * { box-sizing: border-box; margin: 0; padding: 0; }
  html, body {
    width: 1200px; height: 1200px; overflow: hidden;
    background: var(--page-bg);
  }
  .label {
    position: absolute; left: 160px; top: 70px;
    width: 880px; height: 1060px;
    background: var(--label-bg);
    box-shadow: 0 2px 14px rgba(0,0,0,0.08);
    overflow: hidden;
  }
  .fruit-band {
    position: absolute; left: 0; top: 0; width: 100%; height: 198px;
    background: linear-gradient(90deg, var(--fruit-light), var(--fruit) 45%, var(--fruit-dark) 80%, var(--fruit-light));
  }
  .brand-dot {
    position: absolute; left: 112px; top: 145px;
    width: 144px; height: 144px; border-radius: 50%;
    background: var(--fruit);
    border: 8px solid var(--label-bg);
  }
  .brand-lockup {
    position: absolute; left: 120px; top: 856px;
    transform: rotate(-90deg); transform-origin: left top;
    white-space: nowrap;
  }
  .brand-name {
    font-family: "Montserrat", sans-serif; font-weight: 600;
    font-size: 56px; line-height: 1; letter-spacing: 1px;
    color: var(--ink-soft); text-transform: uppercase;
  }
  .brand-tagline {
    font-family: "Montserrat", sans-serif; font-weight: 500;
    font-size: 28px; line-height: 1.05; color: var(--ink-soft);
    padding-left: 64px;
  }
  .fruit-name {
    position: absolute; left: 268px; top: 340px;
    font-family: "Teko", sans-serif; font-weight: 600;
    font-size: 168px; line-height: 1; letter-spacing: 2px;
    color: var(--fruit);
  }
  .product-type {
    position: absolute; left: 270px; top: 478px;
    font-family: "Teko", sans-serif; font-weight: 500;
    font-size: 124px; line-height: 1; letter-spacing: 1px;
    color: var(--ink);
  }
  .origin {
    position: absolute; left: 276px; top: 800px; width: 160px;
    text-align: center;
    font-family: "Teko", sans-serif; font-weight: 400;
    font-size: 36px; line-height: 1; color: var(--ink-soft);
  }
  .origin svg { display: block; margin: 18px auto 0; }
  .batch-card {
    position: absolute; left: 535px; top: 750px; width: 145px;
    font-family: "Teko", sans-serif; font-weight: 400;
    font-size: 24px; line-height: 1; color: var(--ink);
  }
  .batch-card .row { padding: 4px 0; }
  .batch-card .rule { border-top: 2px solid var(--ink); }
  .batch-card .rule-dashed { border-top: 2px dashed var(--ink); }
  .signature {
    height: 50px; margin: 4px 12px;
    background: linear-gradient(90deg, #f3f3f3, #e6e6e6);
  }
  .batch-card .center { text-align: center; }
  .batch-number { color: var(--ink-soft); margin-left: 10px; }
  .facts-rule {
    position: absolute; left: 261px; top: 942px; width: 420px;
    border-top: 3px solid var(--ink);
  }
  .facts {
    position: absolute; left: 261px; top: 958px; width: 420px;
    display: flex; justify-content: space-between;
    font-family: "Teko", sans-serif; font-weight: 500;
    font-size: 40px; line-height: 1; color: var(--ink);
  }
</style>
</head>
<body>
  <main class="label">
    <div class="fruit-band" role="img" aria-label="Band of line-drawn fruit doodles (bananas, pears, apples, citrus slices) on orange"></div>
    <div class="brand-dot"></div>

    <div class="brand-lockup">
      <div class="brand-name">Casa Bellani</div>
      <div class="brand-tagline">liqueur de fruits</div>
    </div>

    <h1 class="fruit-name">ORNAGE</h1>
    <h2 class="product-type">LIQUEUR</h2>

    <div class="origin">
      SWISS-MADE
      <svg width="42" height="42" viewBox="0 0 32 32" aria-label="Swiss flag">
        <rect width="32" height="32" fill="var(--swiss-red)"/>
        <rect x="13" y="6" width="6" height="20" fill="#fff"/>
        <rect x="6" y="13" width="20" height="6" fill="#fff"/>
      </svg>
    </div>

    <div class="batch-card">
      <div class="row center">MASTER CRAFTER:</div>
      <div class="rule"></div>
      <div class="signature" role="img" aria-label="Handwritten signature of the master crafter"></div>
      <div class="rule-dashed"></div>
      <div class="row center">SMALL BATCH</div>
      <div class="rule"></div>
      <div class="row center">BOTTLE:<span class="batch-number">01/25</span></div>
    </div>

    <div class="facts-rule"></div>
    <div class="facts">
      <span>21% ABV</span>
      <span>HOMEMADE</span>
      <span>50CL</span>
    </div>
  </main>
</body>
</html>
```